Football and sports news website

I am looking for a good design and website for a Sports news and Football website. The website will carry mainly football news from different leagues across Europe and the rest of the World. There will be a category for football, tennis, basketball, cricket,ruby. My website should be contemporary and attractive. My favorite colors are blue, purple,orange and red.
Designers can take a clue from http://kelvarodaily.com
There will be column at the under of every news page in which readers of the article can comment.

Industry/Entity Type

News

Coding

Coded - Design and coding required

```html
<!DOCTYPE html>
<html lang="en">
<head>
<meta charset="utf-8">
<title>Stalwart Sports News – Videos</title>
<link href="https://fonts.googleapis.com/css2?family=Roboto:wght@400;500;700&display=swap" rel="stylesheet">
<style>
:root{
  --navy:#00098a;
  --red:#e0261b;
  --dark:#3b3b3b;
  --ink:#2b2b2b;
  --text:#333;
  --muted:#999;
  --line:#e3e3e3;
  --crumb:#6b0f12;
  --arrow:#f08a7a;
}
*{margin:0;padding:0;box-sizing:border-box}
html,body{width:1200px;height:2208px;overflow:hidden;background:#fff}
body{position:relative;font-family:"Roboto",Arial,sans-serif;color:var(--text)}

.site-header{position:absolute;left:0;top:0;width:1200px;height:124px;background:#fff}
.brand{position:absolute;left:122px;top:34px;display:flex;align-items:center;gap:12px}
.brand-dot{width:34px;height:34px;border-radius:50%;background:var(--navy)}
.brand-name{font-size:50px;font-weight:400;color:#111;line-height:1}

.main-nav{position:absolute;left:0;top:124px;width:1200px;height:45px;background:var(--navy);display:flex;align-items:center;padding-left:124px;gap:27px}
.main-nav a{color:#fff;text-decoration:none;font-size:14px}

.page-title{position:absolute;left:112px;top:186px;font-size:32px;font-weight:700;color:var(--ink)}

.video-card{position:absolute;left:130px;width:617px;border:1px solid var(--line);background:#fff}
.video-card h2{position:absolute;left:18px;top:20px;font-size:26px;font-weight:400;color:var(--ink)}
.player{position:absolute;left:18px;top:68px;width:581px}
.player-top{height:7px;background:var(--red)}
.player-screen{position:relative;width:581px}
.progress{height:3px;background:#555}
.progress i{display:block;height:3px;background:#ccc}
.player-controls{height:28px;background:#000;display:flex;align-items:center;padding-left:8px;gap:10px;font-size:13px;color:#fff}
.player-controls .time b{color:var(--red);font-weight:400}
.player-controls .spacer{flex:1}
.player-controls .ctl{width:30px;height:28px;border-left:1px solid #444;display:flex;align-items:center;justify-content:center;margin-left:-10px}
.crumbs{height:18px;display:flex;align-items:center;font-size:8px;background:#f4f4f4}
.crumb{background:var(--crumb);color:#fff;height:14px;line-height:14px;padding:0 8px 0 5px;margin-right:2px;clip-path:polygon(0 0,calc(100% - 5px) 0,100% 50%,calc(100% - 5px) 100%,0 100%)}
.crumbs .current{margin-left:6px;color:#333}
.thumb-strip{height:72px;border-top:1px solid #ddd;border-bottom:3px solid var(--red);display:flex;align-items:center;position:relative}
.thumb-strip .nav{width:22px;display:flex;justify-content:center}
.thumbs{flex:1;display:flex;gap:29px;padding-left:27px}
.thumb{position:relative;width:75px;height:52px;border:2px solid #b3161c;overflow:hidden}
.thumb span{position:absolute;left:0;right:0;bottom:0;background:rgba(0,0,0,.6);color:#fff;font-size:8px;line-height:9px;padding:1px 2px;height:20px;overflow:hidden}
.strip-end{position:absolute;right:0;top:0;width:22px;height:100%;display:flex;align-items:center;justify-content:center;border-left:1px solid #ddd}

.side-panel{position:absolute;left:766px;width:324px;border:1px solid var(--line);background:#fff}
.search{display:flex;position:absolute;left:20px;top:19px}
.search .field{width:241px;height:31px;border:1px solid #ccc;font-size:10px;color:#999;padding:9px 7px}
.search .go{width:43px;height:31px;background:var(--red);display:flex;align-items:center;justify-content:center}

.panel-head{position:absolute;left:20px;width:284px;height:30px;background:var(--dark)}
.panel-head span{display:block;height:30px;width:154px;background:var(--red);color:#fff;font-size:15px;line-height:30px;padding-left:16px;clip-path:polygon(0 0,100% 0,92% 100%,0 100%)}

.sport-list{position:absolute;left:24px;top:69px;list-style:none}
.sport-list li{height:28.5px;display:flex;align-items:center;font-size:11px;font-weight:700;color:#333}
.sport-list li::before{content:"";width:4px;height:4px;border-radius:50%;background:#333;margin-right:10px}
.sport-list svg{margin-right:8px}

.news-list{position:absolute;left:20px;top:62px;width:284px;list-style:none}
.news-item{display:flex;gap:10px;padding:8px 0 10px;border-bottom:1px solid var(--line)}
.news-item:last-child{border-bottom:none}
.news-thumb{width:103px;height:62px;flex:none}
.news-body h3{font-size:12px;font-weight:400;line-height:19px;color:#333}
.meta{display:flex;gap:14px;font-size:9px;color:var(--muted);font-style:italic;margin-top:6px;align-items:center}
.meta svg{margin-right:5px;vertical-align:-2px}

.feature-grid{position:absolute;left:20px;top:67px;display:grid;grid-template-columns:repeat(3,91px);grid-auto-rows:91px;gap:6px}
.tile{position:relative}
.tile .tag{position:absolute;left:0;top:10px;background:var(--red);color:#fff;font-size:11px;padding:2px 4px;line-height:13px}
.tile .tag.b{top:30px}

.to-top{position:absolute;left:1153px;top:2104px}
.site-footer{position:absolute;left:0;top:2172px;width:1200px;height:36px;background:var(--navy);color:#fff;font-size:12px;text-align:center;line-height:36px}
</style>
</head>
<body>

<header class="site-header">
  <div class="brand"><span class="brand-dot"></span><span class="brand-name">Stalwart</span></div>
</header>

<nav class="main-nav">
  <a href="#">Home</a><a href="#">Basketball</a><a href="#">Football</a><a href="#">Tennis</a><a href="#">Contact Us</a>
</nav>

<h1 class="page-title">Videos</h1>

<!-- Football -->
<section class="video-card" style="top:238px;height:607px">
  <h2>Football News</h2>
  <div class="player">
    <div class="player-top"></div>
    <div class="player-screen" role="img" aria-label="Football news video screen, loading" style="height:371px;background:#000">
      <svg style="position:absolute;left:266px;top:192px" width="48" height="40" viewBox="0 0 48 40"><circle cx="24" cy="20" r="6" fill="#fff"/><g stroke="#fff" stroke-width="2" stroke-linecap="round"><path d="M24 8V3M33 11l4-4M36 20h6M33 29l4 4M15 11l-3-3M12 20H4M15 29l-6 6"/></g></svg>
    </div>
    <div class="progress"><i style="width:100%"></i></div>
    <div class="player-controls">
      <svg width="12" height="14" viewBox="0 0 12 14"><path d="M1 1l10 6-10 6z" fill="#fff"/></svg>
      <span class="time"><b>00:38</b> / 00:38</span><span class="spacer"></span>
      <span class="ctl"><svg width="18" height="14" viewBox="0 0 18 14"><path d="M1 5h4l5-4v12l-5-4H1z" fill="#fff"/><path d="M12 4q3 3 0 6M14 2q5 5 0 10" stroke="#fff" fill="none" stroke-width="1.4"/></svg></span>
      <span class="ctl"><svg width="14" height="14" viewBox="0 0 14 14" stroke="#fff" stroke-width="1.6" fill="none"><path d="M1 5V1h4M9 1h4v4M13 9v4H9M5 13H1V9"/></svg></span>
    </div>
    <div class="crumbs"><span class="crumb">Guide</span><span class="crumb">Spot</span><span class="crumb" style="background:var(--red)">Football</span><span class="current">Football News</span></div>
    <div class="thumb-strip">
      <div class="nav"><svg width="8" height="12"><path d="M7 1L2 6l5 5" stroke="#000" stroke-width="2.5" fill="none"/></svg></div>
      <div class="thumbs">
        <div class="thumb" role="img" aria-label="Clip still of a couple at an event" style="background:linear-gradient(135deg,#8a7a6a,#3a2e26)"><span>Pair seen at gala</span></div>
        <div class="thumb" role="img" aria-label="Clip still of a football player" style="background:linear-gradient(135deg,#b03a30,#3b1614)"><span>Lineman drives car into</span></div>
        <div class="thumb" role="img" aria-label="Clip still of a studio segment" style="background:linear-gradient(135deg,#c09a86,#4b3a36)"><span>Sideline Rules: Kick's 10</span></div>
        <div class="thumb" role="img" aria-label="Clip still of a league official" style="background:linear-gradient(135deg,#7a8ab0,#262c3a)"><span>Sideline Rules: League's $31M</span></div>
        <div class="thumb" role="img" aria-label="Clip still of a league shield graphic" style="background:linear-gradient(135deg,#3d4f90,#161c33)"><span>Sideline Rules: Guaranteed</span></div>
      </div>
      <div class="strip-end"><svg width="8" height="12"><path d="M1 1l5 5-5 5" stroke="#000" stroke-width="2.5" fill="none"/></svg></div>
    </div>
  </div>
</section>

<!-- Basketball -->
<section class="video-card" style="top:864px;height:606px">
  <h2>Basketball News</h2>
  <div class="player">
    <div class="player-screen" role="img" aria-label="Basketball match video on an indoor court with arena crowd and scoreboard" style="height:383px;background:linear-gradient(#15151c 0%,#15151c 12%,#3a3038 14%,#b8342c 20%,#8a4a3a 26%,#6f6a6e 34%,#a9865e 48%,#c99a64 66%,#b8885a 80%,#1a1a1a 86%,#111 100%)"></div>
    <div class="progress"><i style="width:84%"></i></div>
    <div class="player-controls">
      <svg width="12" height="14" viewBox="0 0 12 14" fill="#fff"><rect x="1" y="1" width="3.5" height="12"/><rect x="7.5" y="1" width="3.5" height="12"/></svg>
      <span class="time"><b style="color:#777">01:23</b> / 01:43</span><span class="spacer"></span>
      <span class="ctl"><svg width="18" height="14" viewBox="0 0 18 14"><path d="M1 5h4l5-4v12l-5-4H1z" fill="#fff"/><path d="M12 4q3 3 0 6M14 2q5 5 0 10" stroke="#fff" fill="none" stroke-width="1.4"/></svg></span>
      <span class="ctl"><svg width="14" height="14" viewBox="0 0 14 14" stroke="#fff" stroke-width="1.6" fill="none"><path d="M1 5V1h4M9 1h4v4M13 9v4H9M5 13H1V9"/></svg></span>
    </div>
    <div class="crumbs"><span class="crumb">Guide</span><span class="crumb">Spot</span><span class="crumb">Basketball</span><span class="current">CourtLive TV - Youth Cup (U5)</span></div>
    <div class="thumb-strip">
      <div class="nav"><svg width="8" height="12"><path d="M7 1L2 6l5 5" stroke="#000" stroke-width="2.5" fill="none"/></svg></div>
      <div class="thumbs">
        <div class="thumb" role="img" aria-label="Basketball clip still" style="background:linear-gradient(135deg,#c04a30,#5a2a1e)"><span>All Star 5 - Youth U17 World</span></div>
        <div class="thumb" role="img" aria-label="Basketball clip still" style="background:linear-gradient(135deg,#8a8a9a,#2e2e36)"><span>Angola v Serbia - Best Play</span></div>
        <div class="thumb" role="img" aria-label="Basketball clip still" style="background:linear-gradient(135deg,#a88a6a,#3a2e26)"><span>Mexico v Greece - Highlights</span></div>
        <div class="thumb" role="img" aria-label="Basketball clip still" style="background:linear-gradient(135deg,#b09a7a,#3e342c)"><span>Mexico v Greece - Best Block 2</span></div>
        <div class="thumb" role="img" aria-label="Basketball clip still" style="background:linear-gradient(135deg,#6a5a46,#1e1a16)"><span>Tournament Top 10 - Youth U17</span></div>
      </div>
      <div class="strip-end"><svg width="8" height="12"><path d="M1 1l5 5-5 5" stroke="#000" stroke-width="2.5" fill="none"/></svg></div>
    </div>
  </div>
</section>

<!-- Tennis -->
<section class="video-card" style="top:1489px;height:605px">
  <h2>Tennis Tv</h2>
  <div class="player">
    <div class="player-top"></div>
    <div class="player-screen" style="height:48px;background:#000"></div>
    <div class="player-screen" role="img" aria-label="Tennis video of a player at courtside in a packed stadium" style="height:323px;background:linear-gradient(#2e3440 0%,#3e4656 20%,#7a6a76 38%,#a07a86 46%,#4a7ab8 58%,#2a66b0 100%)"></div>
    <div class="progress"><i style="width:5%;background:var(--red)"></i></div>
    <div class="player-controls">
      <svg width="12" height="14" viewBox="0 0 12 14" fill="#fff"><rect x="1" y="1" width="3.5" height="12"/><rect x="7.5" y="1" width="3.5" height="12"/></svg>
      <span class="time"><b>00:06</b> / 02:11</span><span class="spacer"></span>
      <span class="ctl"><svg width="18" height="14" viewBox="0 0 18 14"><path d="M1 5h4l5-4v12l-5-4H1z" fill="#fff"/><path d="M12 4q3 3 0 6M14 2q5 5 0 10" stroke="#fff" fill="none" stroke-width="1.4"/></svg></span>
      <span class="ctl"><svg width="14" height="14" viewBox="0 0 14 14" stroke="#fff" stroke-width="1.6" fill="none"><path d="M1 5V1h4M9 1h4v4M13 9v4H9M5 13H1V9"/></svg></span>
    </div>
    <div class="crumbs"><span class="crumb">Guide</span><span class="crumb">Spot</span><span class="crumb">Tennis</span><span class="current">Harbour Open</span></div>
    <div class="thumb-strip">
      <div class="nav"><svg width="8" height="12"><path d="M7 1L2 6l5 5" stroke="#000" stroke-width="2.5" fill="none"/></svg></div>
      <div class="thumbs">
        <div class="thumb" role="img" aria-label="Tennis clip still" style="background:linear-gradient(135deg,#4aa05a,#1e4a28)"><span>Varela slimed in Melbourne</span></div>
        <div class="thumb" role="img" aria-label="Tennis clip still" style="background:linear-gradient(135deg,#8a6a5a,#2e201a)"><span>Kovar given Melbourne</span></div>
        <div class="thumb" role="img" aria-label="Tennis clip still" style="background:linear-gradient(135deg,#4a6ac0,#1c2c52)"><span>Ferro claims fifth title</span></div>
        <div class="thumb" role="img" aria-label="Tennis clip still" style="background:linear-gradient(135deg,#3a4a8a,#121a33)"><span>Super six for Lina in</span></div>
        <div class="thumb" role="img" aria-label="Tennis clip still" style="background:linear-gradient(135deg,#4a5a9a,#1a2240)"><span>Day nine roundup</span></div>
      </div>
      <div class="strip-end"><svg width="8" height="12"><path d="M1 1l5 5-5 5" stroke="#000" stroke-width="2.5" fill="none"/></svg></div>
    </div>
  </div>
</section>

<!-- Sidebar -->
<aside>
  <div class="side-panel" style="top:186px;height:70px">
    <div class="search">
      <div class="field">Enter a word for search</div>
      <div class="go"><svg width="12" height="12" viewBox="0 0 12 12" fill="none" stroke="#fff" stroke-width="2"><circle cx="5" cy="5" r="3.5"/><path d="M8 8l3 3"/></svg></div>
    </div>
  </div>

  <div class="side-panel" style="top:274px;height:725px">
    <div class="panel-head" style="top:19px"><span>Live Sport News</span></div>
    <ul class="sport-list">
      <li><svg width="14" height="14" viewBox="0 0 14 14"><path d="M2 12L11 3" stroke="#c9a24a" stroke-width="2.4" stroke-linecap="round"/><circle cx="3" cy="4" r="2" fill="#ddd" stroke="#c33" stroke-width=".6"/></svg>Baseball</li>
      <li><svg width="14" height="14" viewBox="0 0 14 14"><circle cx="7" cy="7" r="6" fill="#a0522d"/><path d="M1 7h12M7 1v12" stroke="#5a2a12" stroke-width=".8"/></svg>Handball</li>
      <li><svg width="14" height="14" viewBox="0 0 14 14"><circle cx="7" cy="7" r="6" fill="#fff" stroke="#333"/><path d="M7 4.5l2.4 1.7-.9 2.8h-3l-.9-2.8z" fill="#333"/></svg>Football</li>
      <li><svg width="14" height="14" viewBox="0 0 14 14"><circle cx="7" cy="7" r="6" fill="#b5473a"/><path d="M3 3q4 4 8 8" stroke="#fff" stroke-width=".8" fill="none" stroke-dasharray="1 1"/></svg>Cricket</li>
      <li><svg width="14" height="14" viewBox="0 0 14 14"><circle cx="7" cy="7" r="6" fill="#e0c030"/><path d="M7 1q-3 6 0 12M1 7q6-2 12 0" stroke="#2a5ab0" stroke-width="1.2" fill="none"/></svg>Volleyball</li>
      <li><svg width="14" height="14" viewBox="0 0 14 14"><path d="M2 2h10v6q0 4-5 5-5-1-5-5z" fill="#d9534f"/><path d="M7 4v6M4 7h6" stroke="#fff" stroke-width="1.2"/></svg>Winter sports</li>
      <li><svg width="14" height="14" viewBox="0 0 14 14"><path d="M3 3q0-2 3-2h2q4 0 4 4v3q0 2-2 2H7v3H3z" fill="#c0202a"/></svg>Boxing</li>
      <li><svg width="14" height="14" viewBox="0 0 14 14"><circle cx="7" cy="7" r="6" fill="#e07a20"/><path d="M1 7h12M7 1v12M3 2.5q3 4.5 0 9M11 2.5q-3 4.5 0 9" stroke="#5a2a0a" stroke-width=".7" fill="none"/></svg>Basketball</li>
      <li><svg width="14" height="14" viewBox="0 0 14 14"><circle cx="5" cy="5" r="2.2" fill="#6a9ad0"/><circle cx="10" cy="6" r="2" fill="#e0a030"/><path d="M1 13q4-6 8 0M7 13q3-5 6 0" fill="#6a9ad0"/></svg>Society</li>
      <li><svg width="14" height="14" viewBox="0 0 14 14"><circle cx="4" cy="3.5" r="2" fill="#c04a4a"/><circle cx="10" cy="3.5" r="2" fill="#333"/><path d="M4 6v7M10 6v7M4 8l6 1" stroke="#666" stroke-width="1.6"/></svg>Combat Sports</li>
      <li><svg width="14" height="14" viewBox="0 0 14 14"><path d="M9 1L6 11h-4" stroke="#556" stroke-width="2" fill="none" stroke-linecap="round"/><ellipse cx="11" cy="12" rx="2.5" ry="1.2" fill="#222"/></svg>Ice Hockey</li>
      <li><svg width="14" height="14" viewBox="0 0 14 14"><circle cx="7" cy="7" r="6" fill="#c8e030"/><path d="M2 3q4 4 0 8M12 3q-4 4 0 8" stroke="#fff" stroke-width="1" fill="none"/></svg>Tennis</li>
      <li><svg width="14" height="14" viewBox="0 0 14 14"><circle cx="7" cy="7" r="6" fill="#222"/><circle cx="5" cy="5" r="1.6" fill="#888"/></svg>Snooker</li>
      <li><svg width="14" height="14" viewBox="0 0 14 14"><ellipse cx="7" cy="7" rx="6.5" ry="4" fill="#a0402a"/><path d="M4 7h6" stroke="#fff" stroke-width=".8"/></svg>Aussie Rules</li>
      <li><svg width="14" height="14" viewBox="0 0 14 14"><path d="M6 1v10" stroke="#333" stroke-width="1"/><path d="M6 1l5 2-5 2z" fill="#d33"/><ellipse cx="7" cy="12" rx="5" ry="1.5" fill="#3a9a3a"/></svg>Golf</li>
      <li><svg width="14" height="14" viewBox="0 0 14 14"><ellipse cx="7" cy="7" rx="6.5" ry="4" transform="rotate(-30 7 7)" fill="#b87a3a"/><path d="M5 9l4-4" stroke="#fff" stroke-width=".8"/></svg>Rugby</li>
      <li><svg width="14" height="14" viewBox="0 0 14 14"><rect x="1" y="1" width="12" height="12" fill="#fff" stroke="#333" stroke-width=".6"/><path d="M1 1h3v3H1zM7 1h3v3H7zM4 4h3v3H4zM10 4h3v3h-3zM1 7h3v3H1zM7 7h3v3H7zM4 10h3v3H4zM10 10h3v3h-3z" fill="#222"/></svg>Motorsports</li>
      <li><svg width="14" height="14" viewBox="0 0 14 14"><ellipse cx="7" cy="7" rx="6.5" ry="3.8" transform="rotate(-30 7 7)" fill="#9a5a2a"/><path d="M5 9l4-4M5.5 6.5l1 1M7 5l1 1" stroke="#fff" stroke-width=".8"/></svg>American Football</li>
      <li><svg width="14" height="14" viewBox="0 0 14 14"><circle cx="7" cy="7" r="6" fill="#3a5ad0"/><g fill="#fff"><circle cx="5" cy="5" r="1"/><circle cx="9" cy="5" r="1"/><circle cx="5" cy="9" r="1"/><circle cx="9" cy="9" r="1"/></g></svg>Floorball</li>
      <li><svg width="14" height="14" viewBox="0 0 14 14"><path d="M11 1L4 11q-1 2-3 1" stroke="#7a5a3a" stroke-width="2" fill="none" stroke-linecap="round"/></svg>Bandy</li>
      <li><svg width="14" height="14" viewBox="0 0 14 14"><circle cx="7" cy="7" r="6" fill="#f0b0b0"/><circle cx="7" cy="7" r="3.5" fill="#fff"/><circle cx="7" cy="7" r="1.4" fill="#d33"/></svg>Darts</li>
      <li><svg width="14" height="14" viewBox="0 0 14 14"><path d="M3 11l5-8 3 3z" fill="#e6e6e6" stroke="#aaa" stroke-width=".6"/><circle cx="3" cy="11" r="2" fill="#d88"/></svg>Badminton</li>
    </ul>
  </div>

  <div class="side-panel" style="top:1018px;height:663px">
    <div class="panel-head" style="top:19px"><span>Popular News</span></div>
    <ul class="news-list">
      <li class="news-item"><div class="news-thumb" role="img" aria-label="Photo of a footballer in a white kit" style="background:linear-gradient(135deg,#d0d6de,#8a9a7a)"></div>
        <div class="news-body"><h3>What now for Dale Mercer?</h3><div class="meta"><span><svg width="9" height="9" viewBox="0 0 9 9" fill="none" stroke="#666"><rect x=".5" y="1.5" width="8" height="7"/><path d="M.5 3.5h8"/></svg>July 5, 2016</span><span><svg width="9" height="9" viewBox="0 0 9 9"><path d="M1 1h7v5H4l-2 2V6H1z" fill="#666"/></svg>1</span></div></div></li>
      <li class="news-item"><div class="news-thumb" role="img" aria-label="Photo of two tennis players on grass" style="background:linear-gradient(135deg,#8aaa7a,#3e5a32)"></div>
        <div class="news-body"><h3>Order of play, Day 8: Can Tessa and Mara Quinlan remain on course for final duel?</h3><div class="meta"><span><svg width="9" height="9" viewBox="0 0 9 9" fill="none" stroke="#666"><rect x=".5" y="1.5" width="8" height="7"/><path d="M.5 3.5h8"/></svg>July 5, 2016</span><span><svg width="9" height="9" viewBox="0 0 9 9"><path d="M1 1h7v5H4l-2 2V6H1z" fill="#666"/></svg>0</span></div></div></li>
      <li class="news-item"><div class="news-thumb" role="img" aria-label="Photo of a tennis player in a cap" style="background:linear-gradient(135deg,#d0d0d8,#5a5a66)"></div>
        <div class="news-body"><h3>In defence of Luca Varos – is it really that bad playing video games?</h3><div class="meta"><span><svg width="9" height="9" viewBox="0 0 9 9" fill="none" stroke="#666"><rect x=".5" y="1.5" width="8" height="7"/><path d="M.5 3.5h8"/></svg>July 5, 2016</span><span><svg width="9" height="9" viewBox="0 0 9 9"><path d="M1 1h7v5H4l-2 2V6H1z" fill="#666"/></svg>0</span></div></div></li>
      <li class="news-item"><div class="news-thumb" role="img" aria-label="Photo of a manager at a press conference" style="background:linear-gradient(135deg,#a02020,#2a1a1a)"></div>
        <div class="news-body"><h3>Anton Verelli's first Rovers press conference: LIVE</h3><div class="meta"><span><svg width="9" height="9" viewBox="0 0 9 9" fill="none" stroke="#666"><rect x=".5" y="1.5" width="8" height="7"/><path d="M.5 3.5h8"/></svg>July 5, 2016</span><span><svg width="9" height="9" viewBox="0 0 9 9"><path d="M1 1h7v5H4l-2 2V6H1z" fill="#666"/></svg>0</span></div></div></li>
      <li class="news-item"><div class="news-thumb" role="img" aria-label="Photo of a grass tennis court" style="background:linear-gradient(135deg,#aabb7a,#5a7a3a)"></div>
        <div class="news-body"><h3>Pavel Radic beats Sam Corby to make last four</h3><div class="meta"><span><svg width="9" height="9" viewBox="0 0 9 9" fill="none" stroke="#666"><rect x=".5" y="1.5" width="8" height="7"/><path d="M.5 3.5h8"/></svg>July 6, 2016</span><span><svg width="9" height="9" viewBox="0 0 9 9"><path d="M1 1h7v5H4l-2 2V6H1z" fill="#666"/></svg>0</span></div></div></li>
      <li class="news-item"><div class="news-thumb" role="img" aria-label="Photo of basketball players in an arena" style="background:linear-gradient(135deg,#2a3050,#c8a23a)"></div>
        <div class="news-body"><h3>Island Basketball League:</h3><div class="meta"><span><svg width="9" height="9" viewBox="0 0 9 9" fill="none" stroke="#666"><rect x=".5" y="1.5" width="8" height="7"/><path d="M.5 3.5h8"/></svg>July 6, 2016</span><span><svg width="9" height="9" viewBox="0 0 9 9"><path d="M1 1h7v5H4l-2 2V6H1z" fill="#666"/></svg>0</span></div></div></li>
    </ul>
  </div>

  <div class="side-panel" style="top:1701px;height:274px">
    <div class="panel-head" style="top:17px"><span>Featured News</span></div>
    <div class="feature-grid">
      <div class="tile" role="img" aria-label="Football manager photo" style="background:linear-gradient(135deg,#8a2020,#2a1a1a)"><span class="tag">Football</span><span class="tag b">Top League</span></div>
      <div class="tile" role="img" aria-label="Footballer in white kit photo" style="background:linear-gradient(135deg,#d0d6de,#8a9a7a)"><span class="tag">Football</span></div>
      <div class="tile" role="img" aria-label="Tennis players on grass photo" style="background:linear-gradient(135deg,#8aaa7a,#3e5a32)"><span class="tag">Tennis</span></div>
      <div class="tile" role="img" aria-label="Basketball players photo" style="background:linear-gradient(135deg,#2a3050,#c8a23a)"><span class="tag">Basket Ball</span></div>
      <div class="tile" role="img" aria-label="Tennis player in cap photo" style="background:linear-gradient(135deg,#d0d0d8,#5a5a66)"><span class="tag">Tennis</span></div>
      <div class="tile" role="img" aria-label="Grass tennis court photo" style="background:linear-gradient(135deg,#aabb7a,#5a7a3a)"><span class="tag">Tennis</span></div>
    </div>
  </div>
</aside>

<a class="to-top" href="#" aria-label="Back to top"><svg width="20" height="20" viewBox="0 0 20 20"><path d="M10 2l8 8h-5v8H7v-8H2z" fill="var(--arrow)"/></svg></a>

<footer class="site-footer">Copyright © 2016 Sports News. .</footer>

</body>
</html>
```